Flyer Design

I am a builder that needs a 2 sided colour flyer in DL size that I can post to potential clients that have applied for council approval for construction work.

my website has just been set up, maybe take some ideas from there. www.plankwise.com.au

I have included a good before and after photo that I would like to use

Target Market(s)

people who are thinking of renovating or extending their house

Industry/Entity Type

Construction

```html
<!DOCTYPE html>
<html lang="en">
<head>
<meta charset="utf-8">
<title>Plankwise Pty Ltd – DL Flyer</title>
<link rel="stylesheet" href="https://fonts.googleapis.com/css2?family=Roboto+Condensed:wght@700&family=Open+Sans:wght@400;600&family=PT+Serif:wght@700&display=swap">
<style>
  :root {
    --stage: #3b2d25;
    --plum: #8b1d5e;
    --plum-dark: #6f1549;
    --paper: #f1f1f1;
    --paper-shade: #d9d9d9;
    --navy: #1d3a5c;
    --ink: #3a3a3a;
    --white: #ffffff;
  }
  * { box-sizing: border-box; margin: 0; padding: 0; }
  html, body { width: 1200px; height: 1112px; overflow: hidden; }
  body { background: var(--stage); position: relative; font-family: "Open Sans", Arial, sans-serif; }

  .flyer-side {
    position: absolute;
    left: 129px;
    width: 947px;
    height: 436px;
    overflow: hidden;
    box-shadow: 0 4px 14px rgba(0,0,0,0.45);
  }
  .flyer-front { top: 111px; background: var(--paper); }
  .flyer-back { top: 587px; background: var(--plum); }

  /* front */
  .front-shapes { position: absolute; inset: 0; }
  .brand-name {
    position: absolute; left: 52px; top: 108px;
    font-family: "PT Serif", Georgia, serif; font-weight: 700;
    font-size: 38px; color: var(--navy); letter-spacing: 0.5px;
    display: flex; align-items: center; gap: 12px;
  }
  .brand-mark { width: 22px; height: 22px; background: var(--navy); }
  .license-no {
    position: absolute; left: 836px; top: 80px;
    font-size: 10px; color: var(--plum);
  }
  .headline {
    position: absolute; left: 52px; top: 200px;
    font-family: "Roboto Condensed", "Arial Narrow", sans-serif; font-weight: 700;
    font-size: 40px; line-height: 63px; color: var(--white);
    text-shadow: 2px 2px 3px rgba(0,0,0,0.45);
  }
  .web-address {
    position: absolute; left: 55px; top: 356px;
    font-size: 27px; font-weight: 600; color: var(--ink); letter-spacing: 2px;
  }
  .phone {
    position: absolute; left: 582px; top: 308px;
    font-family: "Roboto Condensed", "Arial Narrow", sans-serif; font-weight: 700;
    font-size: 60px; color: var(--white); letter-spacing: 1px;
  }
  .email {
    position: absolute; left: 584px; top: 384px;
    font-size: 23px; font-weight: 600; color: var(--white); letter-spacing: 1px;
  }

  /* back */
  .intro {
    position: absolute; left: 30px; top: 22px; width: 250px; color: var(--white);
  }
  .intro-title { font-size: 21px; font-weight: 600; line-height: 28px; }
  .intro-copy { margin-top: 12px; font-size: 12.5px; line-height: 18px; text-align: justify; }
  .services { position: absolute; left: 30px; top: 218px; color: var(--white); }
  .services-title { font-size: 21px; font-weight: 600; margin-bottom: 8px; }
  .services-list { list-style: none; }
  .services-list li {
    display: flex; align-items: center; gap: 10px;
    font-size: 14px; line-height: 23px;
  }
  .services-list svg { width: 13px; height: 13px; flex: none; }

  .photo { position: absolute; }
  .photo-front-facade { left: 300px; top: 0; width: 353px; height: 262px;
    background: linear-gradient(180deg, #a9c3dc 0%, #3f4a6b 45%, #2e3550 75%, #5d7a3e 100%); }
  .photo-rear-house { left: 655px; top: 0; width: 292px; height: 262px;
    background: linear-gradient(180deg, #c7d7e8 0%, #b9856c 35%, #d9d4cc 60%, #6d8f3c 100%); }
  .photo-outdoor-living { left: 300px; top: 264px; width: 647px; height: 172px;
    background: linear-gradient(90deg, #d8d2c8 0%, #bfb6a8 40%, #7d5a3e 70%, #5f7d45 100%); }
</style>
</head>
<body>

<section class="flyer-side flyer-front">
  <svg class="front-shapes" width="947" height="436" viewBox="0 0 947 436">
    <defs>
      <linearGradient id="paperFade" x1="0" y1="0" x2="0" y2="1">
        <stop offset="0" stop-color="#ffffff"/>
        <stop offset="1" stop-color="#e4e4e4"/>
      </linearGradient>
      <linearGradient id="tabFade" x1="0" y1="0" x2="1" y2="0">
        <stop offset="0" stop-color="#e2e2e2"/>
        <stop offset="1" stop-color="#ffffff"/>
      </linearGradient>
    </defs>
    <rect width="947" height="436" fill="url(#paperFade)"/>
    <polygon points="0,170 485,170 508,124 947,124 947,132 514,132 491,179 0,179" fill="var(--paper-shade)"/>
    <polygon points="0,179 491,179 514,132 947,132 947,436 0,436" fill="var(--plum)"/>
    <polygon points="0,351 378,351 402,375 378,399 0,399" fill="url(#tabFade)"/>
    <!-- partner badge -->
    <rect x="585" y="35" width="200" height="86" fill="#ffffff"/>
    <circle cx="627" cy="78" r="34" fill="none" stroke="var(--navy)" stroke-width="4"/>
  </svg>

  <div class="brand-name"><span class="brand-mark"></span>PLANKWISE PTY LTD</div>
  <div class="license-no">lic no. 418302C</div>

  <h1 class="headline">Are you thinking of Renovating?<br>You’re In The Right Place!</h1>
  <div class="web-address">www.plankwise.com.au</div>
  <div class="phone">0400 555 218</div>
  <div class="email">hello@plankwise.com.au</div>
</section>

<section class="flyer-side flyer-back">
  <div class="intro">
    <h2 class="intro-title">Extension and<br>Renovation Experts</h2>
    <p class="intro-copy">With over 25 years experience in the building industry, you can feel confident you are making the right choice. You get value for money and peace of mind.</p>
  </div>

  <div class="services">
    <h3 class="services-title">We specialise in:</h3>
    <ul class="services-list">
      <li><svg viewBox="0 0 13 13"><rect x="0.5" y="0.5" width="12" height="12" fill="#fff"/><path d="M3 6.5l2.5 2.5 4.5-5" stroke="var(--plum)" stroke-width="2" fill="none"/></svg>Extensions</li>
      <li><svg viewBox="0 0 13 13"><rect x="0.5" y="0.5" width="12" height="12" fill="#fff"/><path d="M3 6.5l2.5 2.5 4.5-5" stroke="var(--plum)" stroke-width="2" fill="none"/></svg>1st floor additions</li>
      <li><svg viewBox="0 0 13 13"><rect x="0.5" y="0.5" width="12" height="12" fill="#fff"/><path d="M3 6.5l2.5 2.5 4.5-5" stroke="var(--plum)" stroke-width="2" fill="none"/></svg>Home renovations</li>
      <li><svg viewBox="0 0 13 13"><rect x="0.5" y="0.5" width="12" height="12" fill="#fff"/><path d="M3 6.5l2.5 2.5 4.5-5" stroke="var(--plum)" stroke-width="2" fill="none"/></svg>Kitchens</li>
      <li><svg viewBox="0 0 13 13"><rect x="0.5" y="0.5" width="12" height="12" fill="#fff"/><path d="M3 6.5l2.5 2.5 4.5-5" stroke="var(--plum)" stroke-width="2" fill="none"/></svg>Bathrooms</li>
      <li><svg viewBox="0 0 13 13"><rect x="0.5" y="0.5" width="12" height="12" fill="#fff"/><path d="M3 6.5l2.5 2.5 4.5-5" stroke="var(--plum)" stroke-width="2" fill="none"/></svg>Decks and pergolas</li>
      <li><svg viewBox="0 0 13 13"><rect x="0.5" y="0.5" width="12" height="12" fill="#fff"/><path d="M3 6.5l2.5 2.5 4.5-5" stroke="var(--plum)" stroke-width="2" fill="none"/></svg>Outdoor living areas</li>
    </ul>
  </div>

  <div class="photo photo-front-facade" role="img" aria-label="Photo of a renovated two-storey house with dark blue cladding"></div>
  <div class="photo photo-rear-house" role="img" aria-label="Photo of a brick house with tiled roof and front lawn before extension"></div>
  <div class="photo photo-outdoor-living" role="img" aria-label="Photo of a covered outdoor living area with timber deck and dining setting"></div>
</section>

</body>
</html>
```